Flyer für IT-Firma
Zielgruppe
Wir sind eine IT-Firma, die sich unter anderem auf IT-Netzwerke spezialisiert hat. Wir verkaufen Netzwerklösungen, aber auch Produkte im Bereich IT Netzwerk, IT Security, WLAN, Cloud-Lösungen, etc. und Services. Unsere Zielgruppen für diesen Bereich sind kleinere bis Mittlere Unternehmen aber auch öffentliche Verwaltungen, Schulen, Spitäler etc. die ihre IT Netzwerke verbessern möchten und sich absichern möchten für den Fall von WLAN Ausfall oder Datenverlust. Diese Zielgruppen kennen uns womöglich noch nicht oder haben in einem anderen Projekt mit uns zusammengearbeitet. Der Flyer soll sie also von uns und dem Produkt überzeugen.
Aufgabenstellung
Der Flyer soll 2-Seitig oder 4-Seitig sein. Er soll als Vorlage für die Präsentation verschiedenster Produkte dienen. Ziel ist es einen Flyer zu haben im einheitlichen Design, den wir beliebig mit Fotos und Text abfüllen können. So dass wir unsere Produkte und Dienstleistungen im einheitlichen Design vorstellen können. Der Flyer soll folgende Elemente beinhalten:
Seite 1 eher oberflächlich das Produkt vorstellen
- Logo
- Einleitung zum Unternehmen und oder Produkt
- 1-2 Platzhalter für Bilder
- Weiterer Text für Produktbeschreibung
Seite 2 detaillierte Informationen:
- technische Daten (allenfalls in Listenform)
- Weitere Detailinformationen
- Preise
- Kontakt
Vorzugsweise Format A4 damit man auch daraus einfach ein PDF generieren kann und per Mail versenden kann. Vorschläge für andere Formate sind willkommen.

```html
<!DOCTYPE html>
<html lang="de">
<head>
<meta charset="utf-8">
<title>Netvia Systems – Produktflyer</title>
<link href="https://fonts.googleapis.com/css2?family=Catamaran:wght@400;500;600;700&display=swap" rel="stylesheet">
<style>
:root{
  --teal:#14697a;
  --teal-dark:#0f5c6b;
  --green:#6ab04c;
  --orange:#f39325;
  --ink:#2b2b2b;
  --grey:#4a4a4a;
  --sky:#e6f2f8;
  --sky-mid:#cfe4ee;
  --backdrop:#a4a4a4;
  --white:#ffffff;
}
*{margin:0;padding:0;box-sizing:border-box}
html,body{width:960px;height:1200px;overflow:hidden;background:var(--backdrop)}
body{position:relative;font-family:"Catamaran",sans-serif;color:var(--ink)}
.page{position:absolute;width:369px;height:522px;background:var(--white);overflow:hidden}
.p1{left:102px;top:70px}
.p2{left:489px;top:70px}
.p3{left:102px;top:608px}
.p4{left:489px;top:608px;background:var(--sky)}
.abs{position:absolute}
.brand{position:absolute;display:flex;align-items:center;gap:6px;font-weight:600;color:var(--grey);font-size:20px;line-height:1;letter-spacing:-.2px}
.brand .mark{width:9px;height:9px;background:var(--teal)}
.lead{font-size:8.2px;line-height:10px;color:var(--ink)}
.center{text-align:center}
.photo{position:absolute;border-radius:14px;border:3px solid var(--white);box-shadow:0 1px 3px rgba(0,0,0,.2)}

/* page 1 */
.p1 .title{left:196px;top:20px;font-weight:700;font-size:20px;line-height:20px;letter-spacing:.2px}
.p1 .title .t1{color:var(--teal)}
.p1 .title .t2{color:var(--green)}
.p1 .tagline{left:197px;top:63px;width:150px;height:15px;background:var(--orange);color:var(--white);font-size:9.5px;font-weight:600;text-align:center;line-height:16px;border-radius:2px}
.p1 .intro{left:31px;top:88px;width:307px}
.p1 .band{left:0;top:180px;width:369px;height:300px;background:var(--sky-mid);opacity:.55}
.card{position:absolute;top:139px;width:164px;height:342px;border-radius:14px;color:var(--white)}
.card.teal{left:17px;background:var(--teal)}
.card.green{left:188px;background:var(--green)}
.card .photo{left:2px;top:0;width:158px;height:143px}
.card h3{position:absolute;left:15px;top:152px;font-size:11.5px;font-weight:600}
.card .rule{position:absolute;left:15px;top:170px;width:68px;height:1.2px;background:var(--white)}
.card p{position:absolute;left:15px;top:178px;width:138px;font-size:7.9px;line-height:9px}
.p1 .url{left:0;top:492px;width:369px;text-align:center;font-size:12px;letter-spacing:2.4px;color:var(--teal)}
.p1 .url b{font-weight:700}

/* page 2 */
.p2 .bgwave{left:0;top:395px;width:369px;height:130px;background:var(--sky)}
.p2 h2.tech{left:204px;top:26px;font-size:16.5px;font-weight:700;color:var(--green)}
.spec{left:17px;top:58px;width:335px;height:162px;border:2px solid var(--green);border-radius:10px;padding:4px 5px}
.spec table{width:100%;border-collapse:collapse;font-size:6px}
.spec th{background:var(--teal);color:var(--white);font-weight:600;font-size:7.5px;height:15px;border-right:1px solid var(--white)}
.spec th:last-child{border-right:0}
.spec td{text-align:center;height:13.3px;color:var(--ink)}
.spec tr:nth-child(odd) td{background:#eef4f6}
.p2 .rule-g{left:0;top:244px;width:63px;height:2px;background:var(--green)}
.p2 .rule-o{left:305px;top:241px;width:64px;height:2px;background:var(--orange)}
.p2 h2.more{left:0;top:231px;width:369px;text-align:center;font-size:16px;font-weight:700;color:var(--teal)}
.p2 .details{left:30px;top:251px;width:309px;line-height:10px}
.p2 .prices-h{left:26px;top:322px;width:316px;height:20px;background:var(--green);color:var(--white);text-align:center;font-size:11.5px;font-weight:600;line-height:21px;border-radius:2px}
.price{position:absolute;width:156px;height:50px;background:var(--white);border:1.5px solid var(--teal);border-radius:7px;padding:4px 12px}
.price .row{display:flex;justify-content:space-between;font-size:11px;font-weight:600;line-height:13px}
.price .name{color:var(--green)}
.price .amt{color:var(--orange);font-weight:700}
.price p{font-size:5.6px;line-height:7.3px;margin-top:1px}

/* page 3 */
.p3 .photo{left:27px;top:21px;width:138px;height:122px}
.p3 h2{left:28px;top:160px;font-size:14.5px;font-weight:600;color:var(--teal)}
.p3 .uline{left:28px;top:181px;width:38px;height:1.5px;background:var(--green)}
.p3 .col{left:28px;width:153px;font-size:8px;line-height:9.6px}
.p3 .side{left:185px;top:12px;width:184px;height:370px;background:var(--sky);border-radius:26px 0 0 26px}
.p3 .side-h{left:201px;top:21px;width:148px;height:20px;background:var(--green);color:var(--white);text-align:center;font-size:13.5px;font-weight:600;line-height:21px;border-radius:2px}
.p3 .sp{left:201px;width:153px;font-size:8px;line-height:9.6px}
.p3 .gline{left:201px;width:152px;height:1.2px;background:var(--green)}
.steps{left:201px;top:165px;width:153px;list-style:none}
.steps li{display:flex;gap:5px;height:34.5px}
.steps b{color:var(--teal);font-size:10px;font-weight:700;line-height:11px;width:8px}
.steps span{font-size:6.8px;line-height:8.6px}
.p3 .photo2{left:205px;top:369px;width:138px;height:124px}
.p3 .tab1{left:346px;top:405px;width:10px;height:40px;background:var(--teal);border-radius:5px 0 0 5px}
.p3 .tab2{left:352px;top:452px;width:10px;height:25px;background:var(--green);border-radius:5px 0 0 5px}

/* page 4 */
.p4 h2{left:31px;top:7px;font-size:19px;font-weight:600;color:var(--teal)}
.p4 .oline{left:192px;top:29px;width:144px;height:1.5px;background:var(--orange)}
.p4 .intro{left:31px;top:43px;width:310px;font-size:8.3px;line-height:10px}
.feature{left:16px;top:117px;width:336px;height:148px;background:var(--green);border-radius:16px;color:var(--white)}
.feature h3{position:absolute;left:18px;top:10px;font-size:18px;font-weight:600}
.feature p{position:absolute;left:19px;top:37px;width:305px;font-size:8px;line-height:9.6px}
.check{position:absolute;display:flex;gap:8px;align-items:flex-start}
.check svg{width:17px;height:17px;flex:none;margin-top:2px}
.check .t{font-size:15px;font-weight:600;line-height:15px}
.check .s{font-size:8px;line-height:9px}
.p4 .brand4{left:0;top:290px;width:369px;justify-content:center;font-size:30px}
.p4 .brand4 .mark{width:14px;height:14px}
.p4 .thumb{position:absolute;top:343px;width:106px;height:95px;border-radius:10px;border:2px solid var(--white)}
.footer{left:0;top:430px;width:369px;height:92px}
.contact{position:absolute;color:var(--white);font-size:11px;line-height:15.5px}
.contact .ln{display:flex;align-items:center;gap:7px}
.contact svg{width:8px;height:8px;flex:none}
.p4 .divider{left:179px;top:462px;width:1px;height:45px;background:rgba(255,255,255,.35)}
</style>
</head>
<body>

<!-- Seite 1 -->
<section class="page p1">
  <div class="abs band"></div>
  <div class="brand" style="left:29px;top:41px"><span class="mark"></span>netvia systems</div>
  <h1 class="abs title"><span class="t1">LOREM IPSUM</span><br><span class="t2">DOLOR SITAMET</span></h1>
  <div class="abs tagline">Lorem ipsum dolor sit amet</div>
  <p class="abs lead center intro">Lorem ipsum dolor sit amet, consectetur adipiscing elit, sed do eiusmod tempor incididunt ut labore et dolore magna aliqua. Ut enim ad minim veniam, quis nostrud exercitation ullamco laboris nisi ut aliquip ex ea commodo consequat. Duis aute irure dolor in reprehenderit in voluptate velit esse cillum dolore eu fugiat nulla pariatur.</p>

  <article class="card teal">
    <div class="photo" role="img" aria-label="Foto: Netzwerk-Switch mit angeschlossenen Patchkabeln" style="background:linear-gradient(135deg,#1d3f6e,#3f7fbf 55%,#9cc7e6)"></div>
    <h3>Lorem ipsum dolor</h3><div class="rule"></div>
    <p>Lorem ipsum dolor sit amet, consectetur adipiscing elit, sed do eiusmod tempor incididunt ut labore et dolore magna aliqua. Ut enim ad minim veniam, quis nostrud exercitation ullamco laboris nisi ut aliquip ex ea commodo consequat. Duis aute irure dolor in reprehenderit in voluptate velit esse cillum dolore eu fugiat nulla pariatur. Excepteur sint occaecat cupidatat non proident, sunt in culpa qui officia deserunt mollit anim id est laborum. Lorem ipsum dolor sit amet, consectetur adipiscing elit, sed do eiusmod tempor incididunt ut labore et dolore magna aliqua.</p>
  </article>
  <article class="card green">
    <div class="photo" role="img" aria-label="Foto: Hände auf einer Laptop-Tastatur mit leuchtenden Datenströmen" style="background:linear-gradient(135deg,#0c1d3a,#243f86 50%,#8a4fb0 80%,#e0a24a)"></div>
    <h3>Lorem ipsum dolor</h3><div class="rule"></div>
    <p>Lorem ipsum dolor sit amet, consectetur adipiscing elit, sed do eiusmod tempor incididunt ut labore et dolore magna aliqua. Ut enim ad minim veniam, quis nostrud exercitation ullamco laboris nisi ut aliquip ex ea commodo consequat. Duis aute irure dolor in reprehenderit in voluptate velit esse cillum dolore eu fugiat nulla pariatur. Excepteur sint occaecat cupidatat non proident, sunt in culpa qui officia deserunt mollit anim id est laborum. Lorem ipsum dolor sit amet, consectetur adipiscing elit, sed do eiusmod tempor incididunt ut labore et dolore magna aliqua.</p>
  </article>
  <div class="abs url">www.<b>netvia</b>.ch</div>
</section>

<!-- Seite 2 -->
<section class="page p2">
  <div class="abs bgwave"></div>
  <div class="brand" style="left:23px;top:24px"><span class="mark"></span>netvia systems</div>
  <h2 class="abs tech">Technische Daten</h2>
  <div class="abs spec">
    <table>
      <tr><th>Information</th><th>Lorem ipsum</th><th>Lorem ipsum</th><th>Lorem ipsum</th></tr>
      <tr><td>Lorem ipsum dolor</td><td>Lorem ipsum</td><td>Lorem ipsum</td><td>Lorem ipsum</td></tr>
      <tr><td>Lorem ipsum dolor</td><td>Lorem ipsum</td><td>Lorem ipsum</td><td>Lorem ipsum</td></tr>
      <tr><td>Lorem ipsum dolor</td><td>Lorem ipsum</td><td>Lorem ipsum</td><td>Lorem ipsum</td></tr>
      <tr><td>Lorem ipsum dolor</td><td>Lorem ipsum</td><td>Lorem ipsum</td><td>Lorem ipsum</td></tr>
      <tr><td>Lorem ipsum dolor</td><td>Lorem ipsum</td><td>Lorem ipsum</td><td>Lorem ipsum</td></tr>
      <tr><td>Lorem ipsum dolor</td><td>Lorem ipsum</td><td>Lorem ipsum</td><td>Lorem ipsum</td></tr>
      <tr><td>Lorem ipsum dolor</td><td>Lorem ipsum</td><td>Lorem ipsum</td><td>Lorem ipsum</td></tr>
      <tr><td>Lorem ipsum dolor</td><td>Lorem ipsum</td><td>Lorem ipsum</td><td>Lorem ipsum</td></tr>
      <tr><td>Lorem ipsum dolor</td><td>Lorem ipsum</td><td>Lorem ipsum</td><td>Lorem ipsum</td></tr>
      <tr><td>Lorem ipsum dolor</td><td>Lorem ipsum</td><td>Lorem ipsum</td><td>Lorem ipsum</td></tr>
    </table>
  </div>
  <div class="abs rule-g"></div><div class="abs rule-o"></div>
  <h2 class="abs more">Weitere Detailinformationen</h2>
  <p class="abs lead center details">Lorem ipsum dolor sit amet, consectetur adipiscing elit, sed do eiusmod tempor incididunt ut labore et dolore magna aliqua. Ut enim ad minim veniam, quis nostrud exercitation ullamco laboris nisi ut aliquip ex ea commodo consequat.<br>Duis aute irure dolor in reprehenderit in voluptate velit esse cillum dolore eu fugiat nulla pariatur. Excepteur sint occaecat cupidatat non proident, sunt in culpa qui officia deserunt mollit anim id est laborum."</p>
  <div class="abs prices-h">Preise</div>
  <div class="price" style="left:25px;top:347px"><div class="row"><span class="name">Lorem ipsum</span><span class="amt">$0.0</span></div><p>Lorem ipsum dolor sit amet, consectetur adipiscing elit, sed do eiusmod tempor incididunt ut labore et dolore magna aliqua.</p></div>
  <div class="price" style="left:186px;top:347px"><div class="row"><span class="name">Lorem ipsum</span><span class="amt">$0.0</span></div><p>Lorem ipsum dolor sit amet, consectetur adipiscing elit, sed do eiusmod tempor incididunt ut labore et dolore magna aliqua.</p></div>
  <div class="price" style="left:25px;top:400px"><div class="row"><span class="name">Lorem ipsum</span><span class="amt">$0.0</span></div><p>Lorem ipsum dolor sit amet, consectetur adipiscing elit, sed do eiusmod tempor incididunt ut labore et dolore magna aliqua.</p></div>
  <div class="price" style="left:186px;top:400px"><div class="row"><span class="name">Lorem ipsum</span><span class="amt">$0.0</span></div><p>Lorem ipsum dolor sit amet, consectetur adipiscing elit, sed do eiusmod tempor incididunt ut labore et dolore magna aliqua.</p></div>
  <div class="price" style="left:25px;top:453px"><div class="row"><span class="name">Lorem ipsum</span><span class="amt">$0.0</span></div><p>Lorem ipsum dolor sit amet, consectetur adipiscing elit, sed do eiusmod tempor incididunt ut labore et dolore magna aliqua.</p></div>
  <div class="price" style="left:186px;top:453px"><div class="row"><span class="name">Lorem ipsum</span><span class="amt">$0.0</span></div><p>Lorem ipsum dolor sit amet, consectetur adipiscing elit, sed do eiusmod tempor incididunt ut labore et dolore magna aliqua.</p></div>
</section>

<!-- Seite 3 -->
<section class="page p3">
  <div class="photo" role="img" aria-label="Foto: Hand tippt auf eine IoT-Oberfläche mit vernetzten Symbolen" style="background:linear-gradient(135deg,#2c4a66,#5f8fb0 55%,#a9c6d8)"></div>
  <h2 class="abs">Lorem ipsum dolor</h2><div class="abs uline"></div>
  <p class="abs col" style="top:192px">orem ipsum dolor sit amet, consectetur adipiscing elit, sed do eiusmod tempor incididunt ut labore et dolore magna aliqua. Ut enim ad minim veniam, quis nostrud exercitation ullamco laboris nisi ut aliquip ex ea commodo consequat.</p>
  <p class="abs col" style="top:258px">Lorem ipsum dolor sit amet, consectetur adipiscing elit, sed do eiusmod tempor incididunt ut labore et dolore magna aliqua. Ut enim ad minim veniam, quis nostrud exercitation ullamco laboris nisi ut aliquip ex ea commodo consequat. Duis aute irure dolor in reprehenderit in voluptate velit esse cillum dolore eu fugiat nulla pariatur. Excepteur sint occaecat cupidatat non proident, sunt in culpa qui officia deserunt mollit anim id est laborum.</p>
  <p class="abs col" style="top:384px">Lorem ipsum dolor sit amet, consectetur adipiscing elit, sed do eiusmod tempor incididunt ut labore et dolore magna aliqua. Ut enim ad minim veniam, quis nostrud exercitation ullamco laboris nisi ut aliquip ex ea commodo consequat. Duis aute irure dolor in reprehenderit in voluptate velit esse cillum dolore eu fugiat nulla pariatur. Excepteur sint occaecat cupidatat non proident, sunt in culpa qui officia deserunt mollit anim id est laborum.</p>

  <div class="abs side"></div>
  <div class="abs side-h">Lorem ipsum dolor</div>
  <p class="abs sp" style="top:50px">Lorem ipsum dolor sit amet, consectetur adipiscing elit, sed do eiusmod tempor incididunt ut labore et dolore magna aliqua.</p>
  <p class="abs sp" style="top:86px">Lorem ipsum dolor sit amet, consectetur adipiscing elit, sed do eiusmod tempor incididunt ut labore et dolore magna aliqua. Ut enim ad minim veniam, quis nostrud exercitation ullamco laboris nisi ut aliquip ex ea commodo consequat.</p>
  <div class="abs gline" style="top:154px"></div>
  <ol class="abs steps">
    <li><b>1.</b><span>Lorem ipsum dolor sit amet, consectetur adipiscing elit, sed do eiusmod tempor incididunt ut labore et dolore magna aliqua.</span></li>
    <li><b>2.</b><span>Lorem ipsum dolor sit amet, consectetur adipiscing elit, sed do eiusmod tempor incididunt ut labore et dolore magna aliqua.</span></li>
    <li><b>3.</b><span>Lorem ipsum dolor sit amet, consectetur adipiscing elit, sed do eiusmod tempor incididunt ut labore et dolore magna aliqua.</span></li>
    <li><b>4.</b><span>Lorem ipsum dolor sit amet, consectetur adipiscing elit, sed do eiusmod tempor incididunt ut labore et dolore magna aliqua.</span></li>
  </ol>
  <div class="abs gline" style="top:305px"></div>
  <p class="abs sp" style="top:314px">Lorem ipsum dolor sit amet, consectetur adipiscing elit, sed do eiusmod tempor incididunt ut labore et dolore magna aliqua. Ut enim ad minim veniam,</p>
  <div class="abs tab1"></div><div class="abs tab2"></div>
  <div class="photo photo2" role="img" aria-label="Foto: Hand an einem Laptop mit eingeblendeten Marketing-Diagrammen" style="background:linear-gradient(135deg,#1e2b3a,#3b5a78 55%,#7fb0d0)"></div>
</section>

<!-- Seite 4 -->
<section class="page p4">
  <h2 class="abs">Lorem ipsum dolor</h2><div class="abs oline"></div>
  <p class="abs intro">Lorem ipsum dolor sit amet, consectetur adipiscing elit, sed do eiusmod tempor incididunt ut labore et dolore magna aliqua. Ut enim ad minim veniam, quis nostrud exercitation ullamco laboris nisi ut aliquip ex ea commodo consequat. Duis aute irure dolor in reprehenderit in voluptate velit esse cillum dolore eufugiat nulla pariatur. Excepteur sint occaecat cupidatat non proident, sunt in culpa qui officia deserunt mollit anim id est laborum.</p>

  <div class="abs feature">
    <h3>Lorem ipsum dolor</h3>
    <p>Lorem ipsum dolor sit amet, consectetur adipiscing elit, sed do eiusmod tempor incididunt ut labore et dolore magna aliqua. Ut enim ad minim veniam, quis nostrud exercitation ullamco laboris nisi ut aliquip ex ea commodo consequat.</p>
    <div class="check" style="left:19px;top:78px"><svg viewBox="0 0 20 20"><circle cx="10" cy="10" r="9" fill="#fff"/><circle cx="10" cy="10" r="7" fill="#14697a"/><path d="M6 10.3l2.7 2.6L14 7.5" stroke="#fff" stroke-width="2" fill="none"/></svg><div><div class="t">Lorem ipsum</div><div class="s">Lorem ipsum dolor sit amet,</div></div></div>
    <div class="check" style="left:168px;top:78px"><svg viewBox="0 0 20 20"><circle cx="10" cy="10" r="9" fill="#fff"/><circle cx="10" cy="10" r="7" fill="#14697a"/><path d="M6 10.3l2.7 2.6L14 7.5" stroke="#fff" stroke-width="2" fill="none"/></svg><div><div class="t">Lorem ipsum</div><div class="s">Lorem ipsum dolor sit amet,</div></div></div>
    <div class="check" style="left:19px;top:109px"><svg viewBox="0 0 20 20"><circle cx="10" cy="10" r="9" fill="#fff"/><circle cx="10" cy="10" r="7" fill="#14697a"/><path d="M6 10.3l2.7 2.6L14 7.5" stroke="#fff" stroke-width="2" fill="none"/></svg><div><div class="t">Lorem ipsum</div><div class="s">Lorem ipsum dolor sit amet,</div></div></div>
    <div class="check" style="left:168px;top:109px"><svg viewBox="0 0 20 20"><circle cx="10" cy="10" r="9" fill="#fff"/><circle cx="10" cy="10" r="7" fill="#14697a"/><path d="M6 10.3l2.7 2.6L14 7.5" stroke="#fff" stroke-width="2" fill="none"/></svg><div><div class="t">Lorem ipsum</div><div class="s">Lorem ipsum dolor sit amet,</div></div></div>
  </div>

  <div class="brand brand4"><span class="mark"></span>netvia systems</div>

  <svg class="abs footer" viewBox="0 0 369 92" preserveAspectRatio="none"><path d="M0 14 Q184 -4 369 14 V92 H0 Z" fill="#14697a"/></svg>
  <div class="thumb" style="left:22px;background:linear-gradient(135deg,#1a3d6b,#4d86c4 55%,#c9dff0)" role="img" aria-label="Foto: Hände halten eine leuchtende Weltkugel"></div>
  <div class="thumb" style="left:131px;background:linear-gradient(135deg,#12283f,#2f5f8a 55%,#6fa8d0)" role="img" aria-label="Foto: Hand mit vernetzten Lieferketten-Symbolen"></div>
  <div class="thumb" style="left:239px;background:linear-gradient(135deg,#0a1a33,#153a6e 55%,#2f7fcf)" role="img" aria-label="Foto: leuchtendes Cloud-Symbol auf dunklem Hintergrund"></div>

  <div class="contact" style="left:58px;top:457px">
    <div class="ln"><svg viewBox="0 0 10 10"><circle cx="5" cy="5" r="5" fill="#6ab04c"/><path d="M3.3 2.8l1 1-0.6 0.7c0.4 0.8 1 1.4 1.8 1.8l0.7-0.6 1 1-0.8 0.8C4.8 7.3 2.7 5.2 2.5 3.6z" fill="#14697a"/></svg>+41 41 555 01 23</div>
    <div class="ln"><svg viewBox="0 0 10 10"><circle cx="5" cy="5" r="5" fill="#6ab04c"/></svg>sales@netvia.ch</div>
    <div class="ln"><svg viewBox="0 0 10 10"><circle cx="5" cy="5" r="5" fill="#6ab04c"/></svg>www.netvia.ch</div>
  </div>
  <div class="abs divider"></div>
  <div class="contact" style="left:197px;top:457px;line-height:13px">
    <div class="ln"><svg viewBox="0 0 10 12"><path d="M5 0.5a3.8 3.8 0 0 1 3.8 3.8C8.8 7 5 11.5 5 11.5S1.2 7 1.2 4.3A3.8 3.8 0 0 1 5 0.5z" fill="#6ab04c"/><circle cx="5" cy="4.3" r="1.4" fill="#14697a"/></svg>Netvia AG</div>
    <div style="padding-left:15px">Lindenweg 12</div>
    <div style="padding-left:15px">6300 Zug</div>
  </div>
</section>

</body>
</html>
```